Business Card for Pottery and Jewellery Designer

A new business card design is needed to accompany a newly launching pottery and jewellery website. The company logo has been attached for use. The company is called Glazewick Studio. For a sense of the vibe please see the website (it is currently under construction but this way you'll get a feel for the style) www.GlazewickStudio.com

The website font is Pontano Sans for the body of the text with Overlock for headers.

The overall look should be clean and elegant. The back side can have just the logo. The front side should have a smaller logo and the following details displayed:

Glazewick Studio
Designer: Hollis Marrow
Phone: xxx.xxx.xxxx
Email: Designer@GlazewickStudio.com

The structure of displaying this is completely up to you. Different layouts and creative methods of displaying contact info are welcome as long as it stays clean/uncluttered.

No product photographs are to be included in the design as the catalogue changes quickly.

Colour preferences lean towards elegant and understated (charcoal grey, dark navy blue etc.)

Please let me know if you have any further questions or further details required.

Target Market(s)

Target market is 30+ year old women

Industry/Entity Type

Construction

Colors
ffffff
1b1b1b
474747
d9d9d9
fafafa
0355a3

Requirements
Must have
• The submissions so far have looked very typical and don't stand out right now. They're also all in navy with very little variation. I'm looking for something that stands out a it more while still being clean-looking.
Nice to have
• I've attached a few design samples and an idea for a backdrop. It would be great to see some designs in black, white, and grey with only a hint of color.
Should not have
• Product Images

```html
<!DOCTYPE html>
<html lang="en">
<head>
<meta charset="utf-8">
<title>Glazewick Studio – Business Card</title>
<link rel="stylesheet" href="https://fonts.googleapis.com/css2?family=Overlock:wght@400;700&family=Pontano+Sans&display=swap">
<style>
  :root {
    --backdrop: #6e6e6e;
    --card-white: #ffffff;
    --card-black: #000000;
    --navy: #2b2766;
    --ink: #3a3a3a;
    --shadow: rgba(0, 0, 0, 0.45);
  }
  * { margin: 0; padding: 0; box-sizing: border-box; }
  html, body {
    width: 1200px;
    height: 960px;
    overflow: hidden;
    background: var(--backdrop);
  }
  .canvas {
    position: relative;
    width: 1200px;
    height: 960px;
  }
  .card {
    position: absolute;
    top: 165px;
    width: 362px;
    height: 629px;
    box-shadow: 3px 4px 8px var(--shadow);
  }
  .card--front { left: 201px; background: var(--card-white); }
  .card--back  { left: 638px; background: var(--card-black); }

  .brand-mark {
    position: absolute;
    left: 0;
    width: 100%;
    display: flex;
    align-items: center;
    justify-content: center;
    gap: 10px;
    font-family: "Overlock", sans-serif;
    font-weight: 700;
    color: var(--navy);
  }
  .brand-mark__dot {
    border-radius: 50%;
    background: var(--navy);
    flex: none;
  }
  .card--front .brand-mark { top: 180px; font-size: 30px; }
  .card--front .brand-mark__dot { width: 22px; height: 22px; }
  .card--back .brand-mark { top: 270px; font-size: 24px; color: #5a55b5; }
  .card--back .brand-mark__dot { width: 18px; height: 18px; background: #5a55b5; }

  .person {
    position: absolute;
    top: 377px;
    width: 100%;
    text-align: center;
  }
  .person__name {
    font-family: "Overlock", sans-serif;
    font-weight: 700;
    font-size: 17px;
    letter-spacing: 0.3px;
    color: var(--navy);
  }
  .person__role {
    font-family: "Pontano Sans", sans-serif;
    font-size: 13px;
    color: var(--ink);
    margin-top: 1px;
  }

  .contact {
    position: absolute;
    top: 507px;
    width: 100%;
    list-style: none;
    font-family: "Pontano Sans", sans-serif;
    font-size: 14px;
    color: var(--ink);
  }
  .contact__item {
    display: flex;
    justify-content: center;
    align-items: center;
    gap: 6px;
    height: 20px;
  }
  .contact__icon { width: 16px; height: 14px; fill: var(--navy); flex: none; }

  .company-name {
    position: absolute;
    top: 532px;
    width: 100%;
    text-align: center;
    font-family: "Overlock", sans-serif;
    font-size: 27px;
    letter-spacing: 0.5px;
    color: var(--card-white);
  }
</style>
</head>
<body>
<main class="canvas">
  <section class="card card--front" aria-label="Card front">
    <div class="brand-mark"><span class="brand-mark__dot"></span>Glazewick Studio</div>

    <div class="person">
      <p class="person__name">HOLLIS MARROW</p>
      <p class="person__role">Designer</p>
    </div>

    <ul class="contact">
      <li class="contact__item">
        <svg class="contact__icon" viewBox="0 0 16 14" aria-hidden="true">
          <path d="M1 4 C1 1 15 1 15 4 L15 5 L11 5 L11 3.5 L5 3.5 L5 5 L1 5 Z"/>
          <path d="M4 6 L12 6 L14 12 L2 12 Z"/>
        </svg>
        (555) 555.5555
      </li>
      <li class="contact__item">
        <svg class="contact__icon" viewBox="0 0 16 14" aria-hidden="true">
          <rect x="0.5" y="2" width="15" height="10"/>
          <path d="M0.5 2 L8 8 L15.5 2" fill="none" stroke="#fff" stroke-width="1"/>
        </svg>
        Designer@GlazewickStudio.com
      </li>
      <li class="contact__item">
        <svg class="contact__icon" viewBox="0 0 16 16" aria-hidden="true" style="height:16px">
          <circle cx="8" cy="8" r="7.5"/>
          <g fill="none" stroke="#fff" stroke-width="1">
            <ellipse cx="8" cy="8" rx="3" ry="7"/>
            <line x1="1" y1="8" x2="15" y2="8"/>
            <line x1="8" y1="1" x2="8" y2="15"/>
          </g>
        </svg>
        www.GlazewickStudio.com
      </li>
    </ul>
  </section>

  <section class="card card--back" aria-label="Card back">
    <div class="brand-mark"><span class="brand-mark__dot"></span>Glazewick Studio</div>
    <p class="company-name">GLAZEWICK STUDIO</p>
  </section>
</main>
</body>
</html>
```